Bref créative
Business Cards and Letterhead
85 mm x 55 mm / DIN A4 210 mm × 297 mm
Professional
Dominik R. Hartl
Lindenweg 7, 14471 Potsdam
info@lbr-planung.example
www.lbr-planung.example
Please use the standard german sizes for business cards and letters:
85 mm x 55 mm
DIN A4: 210 mm × 297 mm

```html
<!DOCTYPE html>
<html lang="de">
<head>
<meta charset="utf-8">
<title>lbrplanung – Geschäftsausstattung</title>
<link href="https://fonts.googleapis.com/css2?family=Arimo:wght@400;700&display=swap" rel="stylesheet">
<style>
  :root {
    --paper: #ffffff;
    --stage: #ffffff;
    --frame: #d9d9d9;
    --edge: #d4d4d4;
    --ink: #3b3b3b;
    --band: #111111;
    --accent: #f28c1e;
    --stripe-grey: #8c8c8c;
    --band-text: #f2f2f2;
  }
  * { box-sizing: border-box; margin: 0; padding: 0; }
  html, body { width: 1200px; height: 719px; overflow: hidden; background: var(--stage); }
  body { position: relative; font-family: "Arimo", Arial, sans-serif; color: var(--ink); }

  .stage-frame {
    position: absolute; left: 19px; top: 24px; width: 1157px; height: 667px;
    border: 1px solid var(--frame);
  }
  .sheet {
    position: absolute; background: var(--paper);
    border: 1px solid var(--edge);
    box-shadow: 1px 2px 4px rgba(0,0,0,0.12);
    overflow: hidden;
  }

  /* wordmark */
  .wordmark { position: absolute; display: flex; align-items: center; gap: 6px; }
  .wordmark-square { background: var(--accent); flex: none; }
  .wordmark-name { font-weight: 700; color: var(--ink); letter-spacing: 0.5px; line-height: 1; }

  /* black footer band */
  .band { position: absolute; left: 0; right: 0; background: var(--band); color: var(--band-text); }
  .band-stripes { position: absolute; right: 0; display: block; }
  .contact { position: absolute; font-size: 8px; line-height: 1.35; font-weight: 700; }

  /* envelope front */
  .envelope-front { left: 48px; top: 103px; width: 528px; height: 240px; }
  .envelope-front .wordmark { left: 24px; top: 28px; }
  .envelope-front .band { top: 180px; height: 60px; }
  .envelope-front .band-stripes { top: 150px; }
  .envelope-front .contact { left: 18px; top: 10px; }

  /* envelope back */
  .envelope-back { left: 48px; top: 379px; width: 528px; height: 240px; }
  .envelope-back .flap { position: absolute; left: 0; top: 0; }
  .envelope-back .wordmark { left: 50%; top: 44px; transform: translateX(-50%); }

  /* letterhead */
  .letterhead { left: 629px; top: 43px; width: 331px; height: 636px; }
  .letterhead .wordmark { left: 14px; top: 18px; }
  .letterhead .tagline { position: absolute; left: 14px; top: 50px; font-size: 6px; font-weight: 700; color: var(--ink); }
  .letterhead .band { top: 555px; height: 62px; }
  .letterhead .band-stripes { top: 533px; }
  .letterhead .contact { left: 12px; top: 12px; }

  /* business card front */
  .card-front { left: 972px; top: 137px; width: 192px; height: 122px; }
  .card-front .wordmark { left: 10px; top: 12px; }
  .card-front .band { top: 60px; height: 44px; }
  .card-front .band-stripes { top: 48px; }
  .card-front .name-tag {
    position: absolute; left: 10px; top: 62px; padding: 2px 5px;
    background: var(--accent); color: var(--band); font-size: 6.5px; font-weight: 700;
  }
  .card-front .contact { left: 10px; top: 16px; font-size: 4.5px; }

  /* business card back */
  .card-back { left: 972px; top: 283px; width: 192px; height: 125px; }
  .card-back .wordmark { left: 50%; top: 50%; transform: translate(-50%, -50%); }
</style>
</head>
<body>
  <div class="stage-frame"></div>

  <!-- envelope, address side -->
  <section class="sheet envelope-front">
    <div class="wordmark">
      <span class="wordmark-square" style="width:14px;height:14px"></span>
      <span class="wordmark-name" style="font-size:22px">lbrplanung</span>
    </div>
    <svg class="band-stripes" width="170" height="30" viewBox="0 0 170 30">
      <polygon points="30,30 60,0 80,0 50,30" fill="var(--stripe-grey)"/>
      <polygon points="58,30 88,0 118,0 88,30" fill="var(--accent)"/>
      <polygon points="96,30 126,0 170,0 170,30" fill="var(--band)"/>
    </svg>
    <div class="band">
      <p class="contact">Lindenweg 7, 14471 Potsdam<br>
        Phone: (0331) 555 01 42-0 · Fax: (0331) 555 01 42-9<br>
        Email: info@lbr-planung.example · www.lbr-planung.example</p>
    </div>
  </section>

  <!-- envelope, flap side -->
  <section class="sheet envelope-back">
    <svg class="flap" width="528" height="240" viewBox="0 0 528 240">
      <path d="M0,2 Q250,70 264,68 Q278,70 528,2" fill="none" stroke="#c8c8c8" stroke-width="1"/>
    </svg>
    <div class="wordmark">
      <span class="wordmark-square" style="width:14px;height:14px"></span>
      <span class="wordmark-name" style="font-size:22px">lbrplanung</span>
    </div>
  </section>

  <!-- letterhead A4 -->
  <section class="sheet letterhead">
    <div class="wordmark">
      <span class="wordmark-square" style="width:16px;height:16px"></span>
      <span class="wordmark-name" style="font-size:25px">lbrplanung</span>
    </div>
    <p class="tagline">Planung, Beratung und Projektsteuerung</p>
    <svg class="band-stripes" width="130" height="22" viewBox="0 0 130 22">
      <polygon points="20,22 42,0 58,0 36,22" fill="var(--stripe-grey)"/>
      <polygon points="42,22 64,0 88,0 66,22" fill="var(--accent)"/>
      <polygon points="72,22 94,0 130,0 130,22" fill="var(--band)"/>
    </svg>
    <div class="band">
      <p class="contact">Lindenweg 7, 14471 Potsdam<br>
        Phone: (0331) 555 01 42-0 · Fax: (0331) 555 01 42-9<br>
        Email: info@lbr-planung.example · www.lbr-planung.example</p>
    </div>
  </section>

  <!-- business card, front -->
  <section class="sheet card-front">
    <div class="wordmark">
      <span class="wordmark-square" style="width:7px;height:7px"></span>
      <span class="wordmark-name" style="font-size:12px">lbrplanung</span>
    </div>
    <svg class="band-stripes" width="60" height="12" viewBox="0 0 60 12">
      <polygon points="6,12 18,0 26,0 14,12" fill="var(--stripe-grey)"/>
      <polygon points="18,12 30,0 42,0 30,12" fill="var(--accent)"/>
      <polygon points="34,12 46,0 60,0 60,12" fill="var(--band)"/>
    </svg>
    <div class="band">
      <p class="contact">Lindenweg 7, 14471 Potsdam · Geschäftsführer<br>
        Phone: (0331) 555 01 42-0 · Fax: (0331) 555 01 42-9<br>
        info@lbr-planung.example · www.lbr-planung.example</p>
    </div>
    <span class="name-tag">Dominik R. Hartl</span>
  </section>

  <!-- business card, back -->
  <section class="sheet card-back">
    <div class="wordmark">
      <span class="wordmark-square" style="width:10px;height:10px"></span>
      <span class="wordmark-name" style="font-size:17px">lbrplanung</span>
    </div>
  </section>
</body>
</html>
```